Bed Company needs business card

Hello, we are a bed company that makes specialized magnets for beds. We are an alternative healing company. I need a modern and upscale business card. Please incorporate my logo for the card.

Accepted file formats are AI, EPS, and Press-Ready PDFS.

Please include all fonts or convert them to outlines regardless of file type.

If you are designing the card in Photoshop the file Must be 1200dpi.

I am open to anything for the business card.  I really like all of your designs and if you want to change the color of the logo, you can.  I will be making the final selection by Friday.  Thank You for all of your designs.  Feel Free to submit different color logos if you want.  

Reason: I will make a decision Final on Friday April 20th. 2012. Good Luck and Thank you all for the designs.

Target Market(s)

My target Market is people, who are looking for alternative healing.

Industry/Entity Type

Business

Requirements
Must have
• My logo must be incorporated. The front card must have

Name
Job Title

Address
Work
Cell
Fax
email
web

Just put in fake info for the card.

The back of the card. I want the logo on the back with color. I just want it to look modern and cool.

```html
<!DOCTYPE html>
<html lang="en">
<head>
<meta charset="utf-8">
<title>Lodestone Rest – Business Card</title>
<link rel="stylesheet" href="https://fonts.googleapis.com/css2?family=Open+Sans:wght@700;800&display=swap">
<style>
  :root {
    --backdrop: #a0a0a0;
    --navy-top: #07385a;
    --navy-mid: #0b1f6e;
    --royal: #0a14a0;
    --band-blue: #07139a;
    --deep-navy: #060f66;
    --white: #ffffff;
    --band-light: #c9d0ea;
  }
  * { margin: 0; padding: 0; box-sizing: border-box; }
  html, body {
    width: 1200px;
    height: 959px;
    overflow: hidden;
    background: var(--backdrop);
    font-family: "Open Sans", Arial, sans-serif;
    color: var(--white);
  }
  .canvas { position: relative; width: 1200px; height: 959px; }

  .card {
    position: absolute;
    width: 633px;
    height: 361px;
    overflow: hidden;
  }

  /* Logo side */
  .card-logo {
    left: 149px;
    top: 111px;
    background: linear-gradient(to bottom, var(--navy-top) 0%, var(--navy-mid) 40%, var(--royal) 100%);
  }
  .edge-band {
    position: absolute;
    left: 0;
    width: 100%;
    height: 30px;
  }
  .edge-band-top {
    top: 2px;
    background: linear-gradient(to bottom, var(--band-light), var(--white));
  }
  .edge-band-bottom {
    bottom: 2px;
    background: linear-gradient(to bottom, var(--white), var(--band-light));
  }
  .brand {
    position: absolute;
    left: 150px;
    top: 150px;
    display: flex;
    align-items: center;
    gap: 16px;
  }
  .brand-mark {
    width: 40px;
    height: 40px;
    background: var(--white);
  }
  .brand-name {
    font-size: 44px;
    font-weight: 800;
    letter-spacing: -0.5px;
    line-height: 1;
  }

  /* Details side */
  .card-details {
    left: 466px;
    top: 504px;
    background: var(--deep-navy);
  }
  .details-head {
    position: absolute;
    left: 0; top: 0;
    width: 100%;
    height: 138px;
    background: linear-gradient(to bottom, #081488 0%, var(--band-blue) 100%);
  }
  .details-rule {
    position: absolute;
    left: 0; top: 138px;
    width: 100%;
    height: 7px;
    background: var(--white);
  }
  .details-body {
    position: absolute;
    left: 0; top: 145px;
    width: 100%;
    height: 216px;
    background: linear-gradient(to bottom, #050f62 0%, #0a1470 100%);
  }
  .person-name {
    position: absolute;
    left: 270px;
    top: 30px;
    font-size: 19px;
    font-weight: 700;
    letter-spacing: 0.5px;
  }
  .person-title {
    position: absolute;
    left: 326px;
    top: 61px;
    font-size: 9.5px;
    font-weight: 700;
    letter-spacing: 0.3px;
  }
  .contact-list {
    position: absolute;
    left: 352px;
    top: 173px;
    list-style: none;
    font-size: 13px;
    font-weight: 700;
    line-height: 1;
  }
  .contact-list li { position: absolute; white-space: nowrap; }
  .contact-list li:nth-child(1) { top: 0; }
  .contact-list li:nth-child(2) { top: 31px; }
  .contact-list li:nth-child(3) { top: 59px; }
  .contact-list li:nth-child(4) { top: 87px; }
  .online {
    position: absolute;
    left: 90px;
    top: 310px;
    width: 360px;
    text-align: center;
    font-size: 13px;
    font-weight: 700;
    line-height: 22px;
  }
</style>
</head>
<body>
<main class="canvas">

  <section class="card card-logo" aria-label="Card back with brand name">
    <div class="edge-band edge-band-top" role="img" aria-label="Decorative white wave border along the top edge"></div>
    <div class="edge-band edge-band-bottom" role="img" aria-label="Decorative white wave border along the bottom edge"></div>
    <div class="brand">
      <span class="brand-mark" aria-hidden="true"></span>
      <span class="brand-name">Lodestone Rest</span>
    </div>
  </section>

  <section class="card card-details" aria-label="Card front with contact details">
    <div class="details-head"></div>
    <div class="details-rule"></div>
    <div class="details-body"></div>

    <h1 class="person-name">DANIEL HARROW</h1>
    <p class="person-title">MANAGING DIRECTOR</p>

    <ul class="contact-list">
      <li>ADD:HARBOR SQUARE</li>
      <li>WORK: ALTERNATIVE SLEEP HEALING</li>
      <li>CELL:071234598</li>
      <li>FAX:004517280</li>
    </ul>

    <p class="online">daniel@mailbox.com<br>www.restfieldhealing.com</p>
  </section>

</main>
</body>
</html>
```